Plumbing Products Website

This project is to create a web page for Mr. Clear Brook and Mr. Boiler Pro's product offerings. There are 14 unique products. The main page will showcase all 14 products arranged in a clean, concise format that flows nicely and is easy to read.
Furthermore, I need a unique page for each of the 14 products that the main page can link the products to so visitors can click each of them to "Learn More".
For reference, our websites are MrBrookly.example and TopKettleTank.example; so keep the branding, color-scheme, header, footer, etc. consistent with MrBrookly.example and TopKettleTank.example.
For reference, here is the catalog. Feel free to copy as much of the content as necessary to build the pages:
https://online.pageflipper.example/MrBoilerPro/qtrv/
For clarification, the products are:
1. Whole House Water Purification System
2. Whole House Water Ionization System
3. Whole House Water Softener System
4. Water Heater Sediment Pre-Filter
5. Whole-House UV Water Sterilization System
6. The ULTIMATE Whole House Water Treatment System
7. Under-Sink Reverse Osmosis System with UV Sterilizer
8. Smart Water Heater Regulator with Automated Stand-By for Power Savings
9. Whole House Water Pressure Booster
10. Hot Water Heater Tank Volume Booster
11. Leak Detector with Automatic Water Shutoff
12. Whole House UV Air Purification System
13. Leak Detector Alarm with Mobile App
14. Multi-Gas Detector for Carbon Monoxide, Natural Gas, Propane, Methane, Explosive Gasses, Smoke & Fire
Unfortunately, all the content was created by AI, so I don't have any "original" images or other media. I have attached the logos for your reference though. Also, each individual catalog page is attached.
Once the winning design is chosen, I will need the pages coded and hosted on a staging server for me to view in a live environment before I move them to my server.
Let me know if you have any questions.

```html
<!DOCTYPE html>
<html lang="en">
<head>
<meta charset="utf-8">
<title>Mr. Clear Brook &amp; Mr. Boiler Pro — Home Water &amp; Safety Upgrades</title>
<link href="https://fonts.googleapis.com/css2?family=Barlow+Condensed:wght@700;800&family=Inter:wght@400;500;600&display=swap" rel="stylesheet">
<style>
:root{
  --navy:#0c2550;
  --navy-deep:#0a1f45;
  --blue:#1f6fe0;
  --sky:#5aa2ff;
  --orange:#f2871f;
  --orange-dark:#d96d0c;
  --bg-soft:#eef3fa;
  --text:#5a6577;
  --line:#e4e9f1;
  --green:#2fa86a;
  --white:#fff;
}
*{box-sizing:border-box;margin:0;padding:0}
html,body{width:1200px;height:3927px;overflow:hidden}
body{font-family:"Inter",sans-serif;color:var(--text);background:var(--white);font-size:13px}
a{text-decoration:none}
.display{font-family:"Barlow Condensed",sans-serif;font-weight:800;text-transform:uppercase;color:var(--navy);letter-spacing:.2px}
.wrap{width:996px;margin:0 auto;position:relative}
svg{display:block}

/* header */
.site-header{height:104px;background:#fff;display:flex;align-items:center}
.site-header .wrap{display:flex;align-items:center;justify-content:space-between}
.brand{display:flex;align-items:center;gap:10px;font-family:"Barlow Condensed",sans-serif;font-weight:800;font-size:20px;color:var(--navy);width:180px}
.brand .dot{width:34px;height:34px;border-radius:50%;background:var(--blue)}
.nav{display:flex;gap:25px;font-size:12.5px;font-weight:600;color:var(--navy);text-transform:uppercase;letter-spacing:.3px;margin-right:40px}
.btn{display:inline-flex;align-items:center;justify-content:center;gap:8px;font-family:"Barlow Condensed",sans-serif;font-weight:700;text-transform:uppercase;letter-spacing:.8px;font-size:13px;border-radius:5px;color:#fff}
.btn-navy{background:var(--navy);width:165px;height:44px}

/* hero */
.hero{height:515px;position:relative;background:linear-gradient(100deg,#173a78 0%,#2b5aa4 45%,#3c6cb3 70%,#2c5596 100%);overflow:hidden}
.hero::after{content:"";position:absolute;inset:0;background:linear-gradient(180deg,rgba(12,37,80,.15),rgba(12,37,80,.35))}
.hero .wrap{z-index:1;height:100%}
.pill{display:inline-flex;align-items:center;gap:6px;border-radius:20px;font-family:"Barlow Condensed",sans-serif;font-weight:700;font-size:10.5px;letter-spacing:1.2px;text-transform:uppercase;padding:4px 14px}
.hero .pill{position:absolute;top:74px;left:0;background:rgba(31,111,224,.25);border:1px solid rgba(90,162,255,.5);color:var(--sky)}
.hero h1{position:absolute;top:112px;left:0;width:500px;font-size:52px;line-height:53px;color:#fff}
.hero h1 span{color:var(--sky)}
.hero-ctas{position:absolute;top:296px;left:0;display:flex;gap:12px}
.btn-blue{background:var(--blue);height:44px;width:214px}
.btn-ghost{border:2px solid rgba(255,255,255,.8);height:44px;width:190px}
.stats{position:absolute;top:383px;left:0;display:flex;gap:45px}
.stat b{display:block;font-family:"Barlow Condensed",sans-serif;font-weight:800;font-size:30px;color:#fff;line-height:1}
.stat small{font-size:10px;letter-spacing:1px;text-transform:uppercase;color:rgba(255,255,255,.7)}
.why{position:absolute;right:0;top:96px;width:428px;height:317px;border-radius:16px;background:rgba(255,255,255,.1);border:1px solid rgba(255,255,255,.25);padding:28px 27px}
.why h3{font-family:"Barlow Condensed",sans-serif;font-weight:800;font-size:19px;color:#fff;text-transform:uppercase;margin-bottom:14px}
.why li{list-style:none;display:flex;align-items:center;gap:10px;color:#fff;font-size:12.5px;height:32.5px;border-bottom:1px solid rgba(255,255,255,.15)}
.why li:last-child{border:0}
.why .btn{width:100%;height:44px;background:var(--blue);margin-top:22px}

/* product sections */
.section{position:relative;text-align:center}
.section .pill{background:#dbe8fb;border:1px solid #b9d2f5;color:var(--blue)}
.section h2{font-size:35px;margin-top:12px}
.section .lede{font-size:14.5px;line-height:23px;width:630px;margin:12px auto 0}
.water{height:1031px;background:var(--bg-soft);padding-top:67px}
.heater{height:1598px;background:#fff;padding-top:67px}
.grid{display:grid;grid-template-columns:repeat(3,316px);gap:25px 24px;text-align:left;margin-top:45px}
.card{height:349px;background:#fff;border:1px solid var(--line);border-radius:12px;box-shadow:0 6px 18px rgba(12,37,80,.07);display:flex;flex-direction:column}
.card-head{display:flex;gap:14px;padding:22px 22px 17px;border-bottom:1px solid var(--line);height:93px;flex:none}
.ico{width:48px;height:48px;border-radius:10px;flex:none;display:flex;align-items:center;justify-content:center;background:linear-gradient(135deg,#3b8cf2,#1a5fcc)}
.heater .ico{background:linear-gradient(135deg,#fba043,#ec7614)}
.card-head h3{font-family:"Barlow Condensed",sans-serif;font-weight:800;font-size:17px;line-height:17px;color:var(--navy);text-transform:uppercase;max-width:205px}
.card-head p{font-size:11.5px;margin-top:3px}
.card-body{padding:19px 22px 20px;display:flex;flex-direction:column;flex:1}
.desc{font-size:12.5px;line-height:21px;height:46px;max-width:265px}
.feats{list-style:none;margin-top:10px}
.feats li{display:flex;align-items:center;gap:9px;font-size:12px;height:23px;color:#2c3648}
.price{margin-top:auto;display:flex;align-items:flex-end;justify-content:space-between}
.price small{font-size:9.5px;letter-spacing:.8px;text-transform:uppercase}
.price b{display:block;font-family:"Barlow Condensed",sans-serif;font-weight:800;font-size:24px;color:var(--navy);line-height:26px}
.price s{font-size:10.5px;color:#9aa4b4}
.more{display:inline-flex;align-items:center;gap:5px;font-family:"Barlow Condensed",sans-serif;font-weight:700;font-size:12.5px;letter-spacing:.8px;text-transform:uppercase;color:var(--blue);margin-bottom:4px}
.heater .more{color:var(--orange-dark)}

.bundle{position:absolute;left:102px;top:1391px;width:996px;height:134px;border-radius:14px;background:linear-gradient(100deg,#163f86,var(--navy-deep));padding:30px 36px;display:flex;justify-content:space-between;align-items:center;text-align:left}
.bundle h3{font-family:"Barlow Condensed",sans-serif;font-weight:800;font-size:23px;color:#fff;text-transform:uppercase}
.bundle p{color:rgba(255,255,255,.8);font-size:13.5px;line-height:22px;width:480px;margin-top:2px}
.btn-orange{background:var(--orange);border-radius:20px;height:29px;padding:0 16px;font-size:12px;text-transform:none;letter-spacing:.3px}

/* cta */
.cta{height:401px;background:linear-gradient(100deg,#163a78,#21508f 55%,#173c7b);text-align:center;padding-top:75px;position:relative}
.cta .pill{background:rgba(31,111,224,.3);border:1px solid rgba(90,162,255,.5);color:var(--sky)}
.cta h2{font-size:35px;line-height:38px;color:#fff;width:600px;margin:12px auto 0}
.cta p{color:rgba(255,255,255,.85);font-size:14px;line-height:23px;width:640px;margin:14px auto 0}
.cta-btns{display:flex;justify-content:center;gap:16px;margin-top:34px}
.cta .btn-blue{width:190px}
.cta .btn-ghost{width:131px}

/* footer */
.site-footer{height:278px;background:var(--navy-deep);padding-top:62px;color:rgba(255,255,255,.75)}
.foot-cols{display:grid;grid-template-columns:318px 236px 236px 206px;font-size:12px}
.foot-brand .brand{color:#fff;font-size:17px;width:auto;margin-bottom:16px}
.foot-brand .brand .dot{width:26px;height:26px}
.foot-brand p{line-height:19px;width:240px}
.foot-cols h4{font-family:"Barlow Condensed",sans-serif;font-weight:700;font-size:13px;color:#fff;text-transform:uppercase;letter-spacing:.6px;margin:14px 0 8px}
.foot-cols ul{list-style:none}
.foot-cols li{height:23px;display:flex;gap:7px;align-items:flex-start}
.foot-bottom{margin-top:42px;border-top:1px solid rgba(255,255,255,.12);padding-top:20px;display:flex;justify-content:space-between;font-size:11px;color:rgba(255,255,255,.55)}
.foot-bottom span:last-child{color:var(--sky)}
</style>
</head>
<body>

<svg width="0" height="0" style="position:absolute">
  <defs>
    <symbol id="tick" viewBox="0 0 12 12"><path d="M2 6.5l2.5 2.5L10 3.5" stroke="#2fa86a" stroke-width="1.4" fill="none"/></symbol>
    <symbol id="arrow" viewBox="0 0 12 12"><path d="M2 6h8M7 3l3 3-3 3" stroke="currentColor" stroke-width="1.5" fill="none"/></symbol>
  </defs>
</svg>

<header class="site-header">
  <div class="wrap">
    <div class="brand"><span class="dot"></span>Mr. Clear Brook</div>
    <nav class="nav"><span>Water Treatment</span><span>Water Heater Add-Ons</span><span>Bundle &amp; Save</span><span>Get a Quote</span></nav>
    <a class="btn btn-navy">Schedule Install</a>
  </div>
</header>

<section class="hero" role="img" aria-label="Family enjoying clean water in a bright kitchen">
  <div class="wrap">
    <span class="pill">14 Home Water &amp; Safety Upgrades</span>
    <h1 class="display">Cleaner water. <span>Safer home.</span> Every tap, every room.</h1>
    <div class="hero-ctas">
      <a class="btn btn-blue">Browse All Products <svg width="12" height="12" style="color:#fff"><use href="#arrow"/></svg></a>
      <a class="btn btn-ghost">
        <svg width="13" height="13" viewBox="0 0 24 24"><path d="M5 3h4l2 5-3 2a11 11 0 0 0 6 6l2-3 5 2v4a2 2 0 0 1-2 2A17 17 0 0 1 3 5a2 2 0 0 1 2-2z" stroke="#fff" stroke-width="2" fill="none"/></svg>Call 555-014-2290</a>
    </div>
    <div class="stats">
      <div class="stat"><b>14</b><small>Products Available</small></div>
      <div class="stat"><b>4.9★</b><small>2.4K+ Reviews</small></div>
      <div class="stat"><b>100%</b><small>Professionally Installed</small></div>
    </div>
    <div class="why">
      <h3>Why homeowners choose us</h3>
      <ul>
        <li><svg width="12" height="12" viewBox="0 0 12 12"><path d="M2 6l3 3 5-6" stroke="#fff" stroke-width="1.5" fill="none"/></svg>Licensed, insured local technicians</li>
        <li><svg width="12" height="12" viewBox="0 0 12 12"><path d="M2 6l3 3 5-6" stroke="#fff" stroke-width="1.5" fill="none"/></svg>Upfront pricing — no hidden fees</li>
        <li><svg width="12" height="12" viewBox="0 0 12 12"><path d="M2 6l3 3 5-6" stroke="#fff" stroke-width="1.5" fill="none"/></svg>Same-day installation available</li>
        <li><svg width="12" height="12" viewBox="0 0 12 12"><path d="M2 6l3 3 5-6" stroke="#fff" stroke-width="1.5" fill="none"/></svg>Lifetime workmanship warranty</li>
        <li><svg width="12" height="12" viewBox="0 0 12 12"><path d="M2 6l3 3 5-6" stroke="#fff" stroke-width="1.5" fill="none"/></svg>Serving Palm Beach, Broward &amp; the Treasure Coast</li>
      </ul>
      <a class="btn">Get a Free Quote</a>
    </div>
  </div>
</section>

<section class="section water">
  <span class="pill">Mr. Clear Brook</span>
  <h2 class="display">Whole-House Water Treatment</h2>
  <p class="lede">Purification, softening, ionization and sterilization systems that deliver cleaner, safer water to every fixture in your home.</p>
  <div class="wrap grid">
    <article class="card">
      <div class="card-head"><div class="ico"><svg width="20" height="20" viewBox="0 0 24 24"><path d="M4 5h16l-8 14z" stroke="#fff" stroke-width="2" fill="none"/></svg></div><div><h3>Whole-House Water Purification System</h3><p>Mr. Clear Brook</p></div></div>
      <div class="card-body"><p class="desc">Cleaner, better-tasting water at every tap in the house.</p>
        <ul class="feats"><li><svg width="11" height="11"><use href="#tick"/></svg>Sediment &amp; Rust</li><li><svg width="11" height="11"><use href="#tick"/></svg>Chlorine &amp; Chemicals</li><li><svg width="11" height="11"><use href="#tick"/></svg>Heavy Metals</li><li><svg width="11" height="11"><use href="#tick"/></svg>PFAS "Forever Chemicals"</li></ul>
        <div class="price"><div><small>Installed From</small><b>$995</b><s>Reg. $1,500</s></div><a class="more" href="#purification">Learn More <svg width="11" height="11"><use href="#arrow"/></svg></a></div></div>
    </article>
    <article class="card">
      <div class="card-head"><div class="ico"><svg width="20" height="20" viewBox="0 0 24 24"><path d="M3 8q3-3 6 0t6 0 6 0M3 13q3-3 6 0t6 0 6 0M3 18q3-3 6 0t6 0 6 0" stroke="#fff" stroke-width="1.8" fill="none"/></svg></div><div><h3>Whole-House Water Ionization System</h3><p>Mr. Clear Brook</p></div></div>
      <div class="card-body"><p class="desc">Salt-free conditioning that stops scale before it starts.</p>
        <ul class="feats"><li><svg width="11" height="11"><use href="#tick"/></svg>Softer Water</li><li><svg width="11" height="11"><use href="#tick"/></svg>Prevents Limescale</li><li><svg width="11" height="11"><use href="#tick"/></svg>Better Showers</li><li><svg width="11" height="11"><use href="#tick"/></svg>Cleaner Clothes &amp; Dishes</li></ul>
        <div class="price"><div><small>Installed From</small><b>$795</b><s>Reg. $1,200</s></div><a class="more" href="#ionization">Learn More <svg width="11" height="11"><use href="#arrow"/></svg></a></div></div>
    </article>
    <article class="card">
      <div class="card-head"><div class="ico"><svg width="20" height="20" viewBox="0 0 24 24"><path d="M12 3s6 7 6 11a6 6 0 0 1-12 0c0-4 6-11 6-11z" stroke="#fff" stroke-width="2" fill="none"/></svg></div><div><h3>Whole-House Water Softener</h3><p>Mr. Clear Brook</p></div></div>
      <div class="card-body"><p class="desc">Silky-soft water throughout your entire home.</p>
        <ul class="feats"><li><svg width="11" height="11"><use href="#tick"/></svg>Softer, Healthier Skin &amp; Hair</li><li><svg width="11" height="11"><use href="#tick"/></svg>Protects Water Heater &amp; Plumbing</li><li><svg width="11" height="11"><use href="#tick"/></svg>Extends Appliance Life</li><li><svg width="11" height="11"><use href="#tick"/></svg>Spotless Dishes &amp; Glassware</li></ul>
        <div class="price"><div><small>Installed From</small><b>$1,995</b><s>Reg. $3,000</s></div><a class="more" href="#softener">Learn More <svg width="11" height="11"><use href="#arrow"/></svg></a></div></div>
    </article>
    <article class="card">
      <div class="card-head"><div class="ico"><svg width="20" height="20" viewBox="0 0 24 24"><circle cx="12" cy="12" r="4" stroke="#fff" stroke-width="2" fill="none"/><path d="M12 2v3M12 19v3M2 12h3M19 12h3M5 5l2 2M17 17l2 2M5 19l2-2M17 7l2-2" stroke="#fff" stroke-width="2"/></svg></div><div><h3>Whole-House UV Water Sterilizer</h3><p>Mr. Clear Brook</p></div></div>
      <div class="card-body"><p class="desc">Kills 99.99% of viruses, bacteria and organisms.</p>
        <ul class="feats"><li><svg width="11" height="11"><use href="#tick"/></svg>99.99% Effective</li><li><svg width="11" height="11"><use href="#tick"/></svg>Cleaner, Safer Water</li><li><svg width="11" height="11"><use href="#tick"/></svg>Whole-Home Protection</li><li><svg width="11" height="11"><use href="#tick"/></svg>Chemical-Free</li></ul>
        <div class="price"><div><small>Installed From</small><b>$1,495</b><s>Reg. $2,000</s></div><a class="more" href="#uv-sterilizer">Learn More <svg width="11" height="11"><use href="#arrow"/></svg></a></div></div>
    </article>
    <article class="card">
      <div class="card-head"><div class="ico"><svg width="20" height="20" viewBox="0 0 24 24"><path d="M12 3l9 5-9 5-9-5zM3 12l9 5 9-5M3 16l9 5 9-5" stroke="#fff" stroke-width="1.8" fill="none"/></svg></div><div><h3>The Ultimate Whole-House Water System</h3><p>Mr. Clear Brook</p></div></div>
      <div class="card-body"><p class="desc">Purification, ionization and UV sterilization in one solution.</p>
        <ul class="feats"><li><svg width="11" height="11"><use href="#tick"/></svg>1. Whole-House Purification</li><li><svg width="11" height="11"><use href="#tick"/></svg>2. Ionizer, Conditioner &amp; Descaler</li><li><svg width="11" height="11"><use href="#tick"/></svg>3. Whole-House UV Sterilizer</li></ul>
        <div class="price"><div><small>Installed From</small><b>$2,995</b><s>Reg. $4,000</s></div><a class="more" href="#ultimate">Learn More <svg width="11" height="11"><use href="#arrow"/></svg></a></div></div>
    </article>
    <article class="card">
      <div class="card-head"><div class="ico"><svg width="20" height="20" viewBox="0 0 24 24"><path d="M5 4h14v4l-5 5v7h-4v-7L5 8z" stroke="#fff" stroke-width="2" fill="none"/></svg></div><div><h3>Under-Sink Reverse Osmosis with UV</h3><p>Mr. Clear Brook</p></div></div>
      <div class="card-body"><p class="desc">Pure, sterilized drinking water right from your kitchen tap.</p>
        <ul class="feats"><li><svg width="11" height="11"><use href="#tick"/></svg>Reverse Osmosis Filtration</li><li><svg width="11" height="11"><use href="#tick"/></svg>Built-In UV Sterilizer</li><li><svg width="11" height="11"><use href="#tick"/></svg>Fits Under Any Sink</li><li><svg width="11" height="11"><use href="#tick"/></svg>Great-Tasting Water</li></ul>
        <div class="price"><div><small>Installed From</small><b>$895</b><s>Reg. $1,300</s></div><a class="more" href="#reverse-osmosis">Learn More <svg width="11" height="11"><use href="#arrow"/></svg></a></div></div>
    </article>
  </div>
</section>

<section class="section heater">
  <span class="pill">Mr. Boiler Pro</span>
  <h2 class="display">Water Heater &amp; Home Safety Add-Ons</h2>
  <p class="lede">Smart upgrades that stretch your hot water, save energy, catch leaks before they cause damage, and keep your family safe from hazardous gasses.</p>
  <div class="wrap grid">
    <article class="card">
      <div class="card-head"><div class="ico"><svg width="20" height="20" viewBox="0 0 24 24"><path d="M12 3l7 3v6c0 4-3 7-7 9-4-2-7-5-7-9V6z" stroke="#fff" stroke-width="2" fill="none"/></svg></div><div><h3>Water Heater Sediment Pre-Filter</h3><p>Mr. Boiler Pro</p></div></div>
      <div class="card-body"><p class="desc">Stops sediment and rust before they reach your tank.</p>
        <ul class="feats"><li><svg width="11" height="11"><use href="#tick"/></svg>Helps Prevent Tank Corrosion</li><li><svg width="11" height="11"><use href="#tick"/></svg>Protects Heating Elements</li><li><svg width="11" height="11"><use href="#tick"/></svg>Reduces Sediment Buildup</li><li><svg width="11" height="11"><use href="#tick"/></svg>Great Add-On</li></ul>
        <div class="price"><div><small>Installed From</small><b>$495</b><s>Reg. $850</s></div><a class="more" href="#pre-filter">Learn More <svg width="11" height="11"><use href="#arrow"/></svg></a></div></div>
    </article>
    <article class="card">
      <div class="card-head"><div class="ico"><svg width="20" height="20" viewBox="0 0 24 24"><path d="M13 2L5 14h6l-1 8 8-12h-6z" stroke="#fff" stroke-width="2" fill="none"/></svg></div><div><h3>Smart Water Heater Regulator</h3><p>Mr. Boiler Pro</p></div></div>
      <div class="card-body"><p class="desc">Scheduled standby heating that can save up to 50% on energy.</p>
        <ul class="feats"><li><svg width="11" height="11"><use href="#tick"/></svg>Heat Water Only When Needed</li><li><svg width="11" height="11"><use href="#tick"/></svg>Daily &amp; Weekly Schedules</li><li><svg width="11" height="11"><use href="#tick"/></svg>Reduces Standby Waste</li><li><svg width="11" height="11"><use href="#tick"/></svg>Mobile App Included</li></ul>
        <div class="price"><div><small>Installed From</small><b>$395</b><s>Reg. $650</s></div><a class="more" href="#regulator">Learn More <svg width="11" height="11"><use href="#arrow"/></svg></a></div></div>
    </article>
    <article class="card">
      <div class="card-head"><div class="ico"><svg width="20" height="20" viewBox="0 0 24 24"><path d="M4 16a8 8 0 1 1 16 0M12 16l4-5" stroke="#fff" stroke-width="2" fill="none"/></svg></div><div><h3>Whole-House Water Pressure Booster</h3><p>Mr. Boiler Pro</p></div></div>
      <div class="card-body"><p class="desc">Strong, steady pressure from every fixture in the home.</p>
        <ul class="feats"><li><svg width="11" height="11"><use href="#tick"/></svg>Better Showers</li><li><svg width="11" height="11"><use href="#tick"/></svg>Stronger Faucets</li><li><svg width="11" height="11"><use href="#tick"/></svg>Steadier Flow</li><li><svg width="11" height="11"><use href="#tick"/></svg>Ideal For Low-Pressure Homes</li></ul>
        <div class="price"><div><small>Installed From</small><b>$1,495</b><s>Reg. $2,000</s></div><a class="more" href="#pressure-booster">Learn More <svg width="11" height="11"><use href="#arrow"/></svg></a></div></div>
    </article>
    <article class="card">
      <div class="card-head"><div class="ico"><svg width="20" height="20" viewBox="0 0 24 24"><path d="M10 4a2 2 0 0 1 4 0v10a4 4 0 1 1-4 0z" stroke="#fff" stroke-width="2" fill="none"/></svg></div><div><h3>Water Heater Tank Volume Booster</h3><p>Mr. Boiler Pro</p></div></div>
      <div class="card-body"><p class="desc">Up to 50% more hot water without a bigger tank.</p>
        <ul class="feats"><li><svg width="11" height="11"><use href="#tick"/></svg>More Hot Water</li><li><svg width="11" height="11"><use href="#tick"/></svg>Smarter System</li><li><svg width="11" height="11"><use href="#tick"/></svg>Built-In Safety</li><li><svg width="11" height="11"><use href="#tick"/></svg>Save Money</li></ul>
        <div class="price"><div><small>Installed From</small><b>$449</b><s>Reg. $600</s></div><a class="more" href="#volume-booster">Learn More <svg width="11" height="11"><use href="#arrow"/></svg></a></div></div>
    </article>
    <article class="card">
      <div class="card-head"><div class="ico"><svg width="20" height="20" viewBox="0 0 24 24"><path d="M12 3s6 7 6 11a6 6 0 0 1-12 0c0-4 6-11 6-11z" stroke="#fff" stroke-width="2" fill="none"/></svg></div><div><h3>Smart Leak Detector with Automatic Shutoff</h3><p>Mr. Boiler Pro</p></div></div>
      <div class="card-body"><p class="desc">Detects leaks and shuts off your water supply automatically.</p>
        <ul class="feats"><li><svg width="11" height="11"><use href="#tick"/></svg>Real-Time Leak Detection</li><li><svg width="11" height="11"><use href="#tick"/></svg>Automatic Water Shutoff</li><li><svg width="11" height="11"><use href="#tick"/></svg>Mobile App Alerts</li><li><svg width="11" height="11"><use href="#tick"/></svg>Water Usage Monitoring</li></ul>
        <div class="price"><div><small>Installed From</small><b>$995</b><s>Reg. $1,500</s></div><a class="more" href="#leak-shutoff">Learn More <svg width="11" height="11"><use href="#arrow"/></svg></a></div></div>
    </article>
    <article class="card">
      <div class="card-head"><div class="ico"><svg width="20" height="20" viewBox="0 0 24 24"><path d="M3 9h12a3 3 0 1 0-3-3M3 14h16a3 3 0 1 1-3 3" stroke="#fff" stroke-width="2" fill="none"/></svg></div><div><h3>Whole-House UV Air Purification System</h3><p>Mr. Boiler Pro</p></div></div>
      <div class="card-body"><p class="desc">Dual UV-C lights continuously sanitize the air in your HVAC system.</p>
        <ul class="feats"><li><svg width="11" height="11"><use href="#tick"/></svg>Inactivates Bacteria &amp; Viruses</li><li><svg width="11" height="11"><use href="#tick"/></svg>Targets Airborne Microorganisms</li><li><svg width="11" height="11"><use href="#tick"/></svg>Disrupts DNA/RNA</li><li><svg width="11" height="11"><use href="#tick"/></svg>Hidden Installation</li></ul>
        <div class="price"><div><small>Installed From</small><b>$395</b><s>Reg. $800</s></div><a class="more" href="#uv-air">Learn More <svg width="11" height="11"><use href="#arrow"/></svg></a></div></div>
    </article>
    <article class="card">
      <div class="card-head"><div class="ico"><svg width="20" height="20" viewBox="0 0 24 24"><path d="M3 9a13 13 0 0 1 18 0M6 13a8 8 0 0 1 12 0M9 16.5a3.5 3.5 0 0 1 6 0" stroke="#fff" stroke-width="2" fill="none"/><circle cx="12" cy="19.5" r="1.3" fill="#fff"/></svg></div><div><h3>Leak Detector Alarm with Mobile App</h3><p>Mr. Boiler Pro</p></div></div>
      <div class="card-body"><p class="desc">Instant leak alerts to your phone, anytime, anywhere.</p>
        <ul class="feats"><li><svg width="11" height="11"><use href="#tick"/></svg>Instant Leak Detection</li><li><svg width="11" height="11"><use href="#tick"/></svg>Mobile App Alerts</li><li><svg width="11" height="11"><use href="#tick"/></svg>Wi-Fi Connected</li><li><svg width="11" height="11"><use href="#tick"/></svg>Long Battery Life</li></ul>
        <div class="price"><div><small>Installed From</small><b>$195</b><s>Reg. $350</s></div><a class="more" href="#leak-alarm">Learn More <svg width="11" height="11"><use href="#arrow"/></svg></a></div></div>
    </article>
    <article class="card">
      <div class="card-head" style="height:76px"><div class="ico"><svg width="20" height="20" viewBox="0 0 24 24"><path d="M6 3h8l4 4v14H6zM14 3v4h4M9 12h6M9 16h6" stroke="#fff" stroke-width="1.8" fill="none"/></svg></div><div><h3>Multi-Gas &amp; Fire Detector</h3><p>Mr. Boiler Pro</p></div></div>
      <div class="card-body"><p class="desc">One smart alarm for gas, carbon monoxide, smoke &amp; fire.</p>
        <ul class="feats"><li><svg width="11" height="11"><use href="#tick"/></svg>Detects Invisible Dangers</li><li><svg width="11" height="11"><use href="#tick"/></svg>Loud Alarm Alerts</li><li><svg width="11" height="11"><use href="#tick"/></svg>Digital Display</li><li><svg width="11" height="11"><use href="#tick"/></svg>Great Add-On</li></ul>
        <div class="price"><div><small>Installed From</small><b>$195</b><s>Reg. $300</s></div><a class="more" href="#multi-gas">Learn More <svg width="11" height="11"><use href="#arrow"/></svg></a></div></div>
    </article>
  </div>
  <div class="bundle">
    <div><h3>Bundle 2 or more upgrades &amp; save 20%</h3><p>Already scheduling one install? Ask your technician about combining products — many upgrades qualify for same-day installation.</p></div>
    <a class="btn btn-orange">Ask About Bundling →</a>
  </div>
</section>

<section class="cta" role="img" aria-label="Family in a kitchen drinking filtered water, under a blue overlay">
  <span class="pill">Get Started</span>
  <h2 class="display">Get clean, safe water &amp; peace of mind today</h2>
  <p>Call now or request a quote and a licensed technician will help you choose the right system for your home.</p>
  <div class="cta-btns">
    <a class="btn btn-blue"><svg width="13" height="13" viewBox="0 0 24 24"><path d="M5 3h4l2 5-3 2a11 11 0 0 0 6 6l2-3 5 2v4a2 2 0 0 1-2 2A17 17 0 0 1 3 5a2 2 0 0 1 2-2z" stroke="#fff" stroke-width="2" fill="none"/></svg>Call 555-014-2290</a>
    <a class="btn btn-ghost"><svg width="13" height="13" viewBox="0 0 24 24"><rect x="3" y="5" width="18" height="14" rx="2" stroke="#fff" stroke-width="2" fill="none"/><path d="M3 7l9 6 9-6" stroke="#fff" stroke-width="2" fill="none"/></svg>Email Us</a>
  </div>
</section>

<footer class="site-footer">
  <div class="wrap">
    <div class="foot-cols">
      <div class="foot-brand"><div class="brand"><span class="dot"></span>Mr. Clear Brook</div><p>Water purification and water heater specialists serving Palm Beach, Broward, and the Treasure Coast. Professionally installed, backed for life.</p></div>
      <div><h4>Products</h4><ul><li>Water Treatment</li><li>Water Heater Add-Ons</li><li>Bundle &amp; Save</li><li>View All 14 Products</li></ul></div>
      <div><h4>Company</h4><ul><li>MrBrookly.example</li><li>TopKettleTank.example</li><li>About Us</li><li>Contact Us</li></ul></div>
      <div><h4>Get in Touch</h4><ul>
        <li><svg width="11" height="11" viewBox="0 0 24 24"><path d="M5 3h4l2 5-3 2a11 11 0 0 0 6 6l2-3 5 2v4a2 2 0 0 1-2 2A17 17 0 0 1 3 5a2 2 0 0 1 2-2z" stroke="#5aa2ff" stroke-width="2" fill="none"/></svg>555-014-2290</li>
        <li><svg width="11" height="11" viewBox="0 0 24 24"><rect x="3" y="5" width="18" height="14" rx="2" stroke="#5aa2ff" stroke-width="2" fill="none"/><path d="M3 7l9 6 9-6" stroke="#5aa2ff" stroke-width="2" fill="none"/></svg>info@topkettletank.example</li>
        <li style="height:auto;line-height:15px"><svg width="11" height="11" viewBox="0 0 24 24" style="flex:none;margin-top:2px"><path d="M12 22s7-7 7-12a7 7 0 0 0-14 0c0 5 7 12 7 12z" stroke="#5aa2ff" stroke-width="2" fill="none"/><circle cx="12" cy="10" r="2.5" stroke="#5aa2ff" stroke-width="2" fill="none"/></svg>4821 Larkspur Way, Suite 3, Coral Vista, FL</li>
      </ul></div>
    </div>
    <div class="foot-bottom"><span>© 2026 Mr. Clear Brook &amp; Mr. Boiler Pro. All Rights Reserved.</span><span>Licensed &amp; Insured Plumbing Professionals</span></div>
  </div>
</footer>

</body>
</html>
```